Quill Yard Profile Banner Needed

I am in need of a Quill Yard Banner photo for my profile. The dimensions are 1584 x 396 pixels and the bottom left is where Quill Yard places my photo over so be aware of that. I attached an example for your reference.

I have also attached my logo and business card so you can keep the same color & style conistant.

Also add the following text:

"Preserve capital with a tax advantaged lease for equipment, vehicles, software and more! $5,000 - $50m"

You can also look at our website here:
www.HarborBrookFunding.example

```html
<!DOCTYPE html>
<html lang="en">
<head>
<meta charset="utf-8">
<title>Harbor Brook Funding – Profile Banner</title>
<link rel="stylesheet" href="https://fonts.googleapis.com/css2?family=Montserrat:wght@500&family=Crimson+Text:wght@400;600&display=swap">
<style>
  :root {
    --page-bg: #ffffff;
    --navy-left: #262540;
    --navy-right: #15133a;
    --navy-deep: #1a1940;
    --building: #1c2050;
    --white: #ffffff;
    --cyan: #4cc6e8;
    --rule: #2b7fb0;
    --photo-top: #4a4e58;
    --photo-bottom: #1f2a3c;
  }
  * { margin: 0; padding: 0; box-sizing: border-box; }
  html, body {
    width: 1043px; height: 1200px; overflow: hidden;
    background: var(--page-bg);
  }
  .canvas { position: relative; width: 1043px; height: 1200px; }

  .banner {
    position: absolute; left: 41px; top: 470px;
    width: 960px; height: 240px;
    background: linear-gradient(90deg, var(--navy-left) 0%, var(--navy-deep) 55%, var(--navy-right) 100%);
    box-shadow: 0 6px 18px rgba(0,0,0,0.25);
  }
  .banner__buildings { position: absolute; left: 715px; top: 0; width: 220px; height: 240px; }

  .banner__photo {
    position: absolute; left: 755px; top: 24px;
    width: 145px; height: 189px; border-radius: 14px;
    background: linear-gradient(170deg, var(--photo-top) 0%, #2e3646 45%, var(--photo-bottom) 100%);
    box-shadow: 0 4px 12px rgba(0,0,0,0.45);
  }

  .banner__content {
    position: absolute; left: 293px; top: 22px; width: 374px;
    text-align: center; color: var(--white);
  }
  .brand {
    display: flex; align-items: center; justify-content: center; gap: 10px;
    height: 62px;
  }
  .brand__mark { width: 14px; height: 14px; background: var(--cyan); }
  .brand__name {
    font-family: "Montserrat", sans-serif; font-weight: 500;
    font-size: 23px; letter-spacing: 0.5px; color: var(--white);
    text-transform: uppercase;
  }
  .rule { height: 1px; background: var(--rule); margin: 12px 0 0; }
  .tagline {
    font-family: "Crimson Text", serif; font-size: 17px; line-height: 21px;
    margin-top: 6px;
  }
  .price {
    font-family: "Crimson Text", serif; font-weight: 600;
    font-size: 20px; line-height: 24px; color: var(--cyan);
    display: flex; align-items: center; justify-content: center; gap: 4px;
  }
  .price svg { width: 13px; height: 13px; }
  .rule--lower { margin-top: 6px; }
  .website {
    font-family: "Crimson Text", serif; font-size: 16px; margin-top: 8px;
  }
  .website__accent { color: var(--cyan); }

  .avatar {
    position: absolute; left: 53px; top: 613px;
    width: 186px; height: 186px; border-radius: 50%;
    background: radial-gradient(circle at 40% 35%, #22214a 0%, var(--navy-right) 100%);
    border: 6px solid var(--white);
    display: flex; align-items: center; justify-content: center; text-align: center;
  }
  .avatar__name {
    font-family: "Montserrat", sans-serif; font-weight: 500;
    font-size: 19px; line-height: 24px; color: var(--white);
    text-transform: uppercase;
  }
</style>
</head>
<body>
<main class="canvas">
  <section class="banner">
    <svg class="banner__buildings" viewBox="0 0 220 240" aria-hidden="true">
      <polygon points="0,42 45,30 45,240 0,240" fill="var(--building)" opacity="0.8"/>
      <polygon points="160,50 215,78 215,240 160,240" fill="var(--building)" opacity="0.8"/>
    </svg>
    <div class="banner__photo" role="img" aria-label="Portrait photo of the account holder"></div>

    <div class="banner__content">
      <div class="brand">
        <span class="brand__mark"></span>
        <span class="brand__name">Harbor Brook Funding</span>
      </div>
      <div class="rule"></div>
      <p class="tagline">Preserve capital with a tax advantaged lease for equipment, vehicles, software and more!</p>
      <p class="price">
        <svg viewBox="0 0 20 20" aria-hidden="true"><path d="M10 0 L12 8 L20 10 L12 12 L10 20 L8 12 L0 10 L8 8 Z" fill="var(--cyan)"/></svg>
        $5,000 - $50m
      </p>
      <div class="rule rule--lower"></div>
      <p class="website">www.Harbor<span class="website__accent">Brook</span>Funding.example</p>
    </div>
  </section>

  <div class="avatar">
    <span class="avatar__name">Harbor<br>Brook<br>Funding</span>
  </div>
</main>
</body>
</html>
```